Funky Modern Flyer A5 or Postcard size

Hi, I am looking at a one small flyer (A5 or postcard size) that I can put both on my website on the front page (ie so png) and also send out if necessary.

It has to be modern, funky and hip. My brand is professional / Corporate so it also has to fit in with that brand.

There are 6 attachments:
Example 1 - Kavorra - I like this look, clean, modern, funky and says it all.
Example 2 - Kavora - again another look I like, simple, explanatory
Example 4 - Artisan Bazaar - font is cool on this one but background not so much too much going on but I like the font
Example 5 - Example 4 - Artisan Bazaar - font is cool on this one but background not so much too much going on but I like the font
5 is my logo
Example 6 is something I found on the web this morning which is effective.

It is for a Mentoring and Training program I run called: SKYWARD

What is to be included is the following:
The name: Skyward
Somewhere: Training, Mentoring
My Logo (see attached two options) you can choose which colour suits and I have the source file should you need it
My website and email: www.deliamarsk.example / delia@deliamarsk.example

This wording: This is one of our highest in-demand programs and is based on a background and proven track record by Delia in accelerating sales organisations and their people into stand out high performers. **(NOTE this wording in this paragraph may change and I am open to you changing if you think you can make it more effective!)

Colours: white, black and gold (those are our website colours).

I'd like the Skyward to really stand out.... I have included two fonts that I really like that I got off Artisan Bazaar. However, feel free to suggest other fonts that you think cool or funky!
Updates

Hi everyone, just to add a note to the brief, I am not overly keen on pictures that are really busy. I only like a picture that is minimal and effective. The examples from Artisan Bazaar was more for the Font Style not so much the pictures in the background. The pictures can take away from a design unless done really minimally.....hope this makes sense. Delia Added Wednesday, March 15, 2017

Target Market(s)

My target Market is Corporates but I want a Funky Modern look as a lot of people in Corporates are Millennials as well which is part of my target market

Industry/Entity Type

Information Technology

Requirements
Must have
• What is to be included is the following:
• The name: Skyward
• Somewhere: Training, Mentoring
• My Logo (see attached two options) you can choose which colour suits and I have the source file should you need it
• My website and email: www.deliamarsk.example / delia@deliamarsk.example
• This wording: This is one of our highest in-demand programs and is based on a background and proven track record in high performance and accelerating sales organisations and their people into stand out high performers. (**NOTE this wording may change when final design is picked to be changed as still working in it***)
• Colours: white, black and gold (those are our website colours).
• I'd like the Skyward to really stand out.... I have included two fonts that I really like that I got off Artisan Bazaar. However, feel free to suggest other fonts that you think cool or funky! NOTE: The pictures I have attached is mainly for the FONTS not for the background pictures. I am not that keen on background pictures as it can take away from the font - unless it is minimal
Should not have
• Too many different colours, I like slick, modern, clean. White, gold and black preferred as this is our website colour.
• NOTE: The pictures from Artisan Bazaar I have attached are mainly for the FONTS not for the background pictures. I am not hugely keen on background pictures as it can take away from the font/message - unless the pictures are minimal but effective.

```html
<!DOCTYPE html>
<html lang="en">
<head>
<meta charset="utf-8">
<title>Skyward – Training, Mentoring flyers</title>
<link rel="stylesheet" href="https://fonts.googleapis.com/css2?family=Kaushan+Script&family=Montserrat:wght@400&family=Oswald:wght@300&display=swap">
<style>
  :root {
    --page-bg: #ececec;
    --flyer-bg: #262626;
    --band-dark: #0b0b0b;
    --band-light: #9a9a9a;
    --frame-line: #141414;
    --silver: #d9d9d9;
    --silver-soft: #bdbdbd;
    --white: #ffffff;
    --figure-tone: #b5b5b5;
    --decor-tone: #1a1a1a;
  }
  * { box-sizing: border-box; margin: 0; padding: 0; }
  html, body { width: 1200px; height: 836px; overflow: hidden; }
  body {
    position: relative;
    background: var(--page-bg);
    font-family: "Oswald", "Arial Narrow", sans-serif;
  }
  .flyer {
    position: absolute;
    top: 28px;
    width: 536px;
    height: 760px;
    background: var(--flyer-bg);
    overflow: hidden;
    color: var(--silver);
  }
  .flyer--solo { left: 30px; }
  .flyer--group { left: 623px; }
  .flyer__art { position: absolute; inset: 0; }
  .flyer__frame {
    position: absolute;
    left: 26px; top: 26px; right: 26px; bottom: 26px;
    border: 1px solid var(--frame-line);
  }
  .brand-name {
    position: absolute;
    top: 112px; left: 0; right: 0;
    text-align: center;
    font-family: "Montserrat", "Helvetica", sans-serif;
    font-weight: 400;
    font-size: 29px;
    letter-spacing: 1px;
    color: var(--silver);
  }
  .figure {
    position: absolute;
    background: var(--figure-tone);
    opacity: .75;
    border-radius: 40% 40% 20% 20%;
  }
  .figure--runner { left: 254px; top: 180px; width: 56px; height: 148px; }
  .figure--group { left: 141px; top: 174px; width: 220px; height: 150px; }
  .decor-pieces {
    position: absolute;
    left: 381px; top: 44px; width: 140px; height: 248px;
    background: linear-gradient(180deg, rgba(20,20,20,.2), rgba(10,10,10,.7));
  }
  .program-title {
    position: absolute;
    left: 40px; top: 300px; width: 460px;
    text-align: center;
    font-family: "Kaushan Script", cursive;
    font-size: 92px;
    line-height: 1;
    transform: rotate(-10deg);
  }
  .flyer--solo .program-title { color: var(--silver); }
  .flyer--group .program-title { color: var(--white); }
  .program-tagline {
    position: absolute;
    left: 250px; top: 460px;
    font-family: "Kaushan Script", cursive;
    font-size: 24px;
    color: var(--white);
    transform: rotate(-12deg);
    text-shadow: 1px 2px 2px rgba(0,0,0,.6);
  }
  .program-summary {
    position: absolute;
    left: 40px; right: 40px; top: 606px;
    text-align: center;
    text-transform: uppercase;
    font-size: 15px;
    line-height: 24px;
    color: var(--silver);
  }
  .contact {
    position: absolute;
    left: 0; right: 0; top: 698px;
    display: flex;
    justify-content: center;
    gap: 18px;
    font-size: 15px;
    letter-spacing: .6px;
    text-transform: uppercase;
    color: var(--silver);
  }
  .contact__item { display: flex; align-items: center; gap: 7px; }
  .contact__icon { width: 13px; height: 13px; }
</style>
</head>
<body>
<svg width="0" height="0" style="position:absolute">
  <defs>
    <filter id="grain" x="0" y="0" width="100%" height="100%">
      <feTurbulence type="fractalNoise" baseFrequency="0.9" numOctaves="2" result="noise"/>
      <feColorMatrix type="saturate" values="0"/>
      <feComponentTransfer><feFuncA type="linear" slope="0.18"/></feComponentTransfer>
    </filter>
  </defs>
</svg>

<section class="flyer flyer--solo">
  <svg class="flyer__art" width="536" height="760" viewBox="0 0 536 760">
    <polygon points="0,276 536,212 536,420 0,532" fill="var(--band-dark)"/>
    <rect width="536" height="760" filter="url(#grain)"/>
  </svg>
  <div class="flyer__frame"></div>
  <div class="brand-name">DELIA MARSK</div>
  <div class="figure figure--runner" role="img" aria-label="Silhouette of a leaping runner"></div>
  <h1 class="program-title">Skyward</h1>
  <svg class="flyer__art" width="536" height="760" viewBox="0 0 536 760">
    <path d="M190 506 Q330 450 476 392" stroke="var(--silver-soft)" stroke-width="6" fill="none" stroke-linecap="round"/>
  </svg>
  <p class="program-tagline">Training, Mentoring</p>
  <p class="program-summary">This is one of our highest in-demand programs and is based on a background and proven track record by Delia in accelerating sales organisations and their people into stand out high performers.</p>
  <div class="contact">
    <span class="contact__item">
      <svg class="contact__icon" viewBox="0 0 14 14" fill="none" stroke="currentColor"><circle cx="7" cy="7" r="6"/><ellipse cx="7" cy="7" rx="2.6" ry="6"/><line x1="1" y1="7" x2="13" y2="7"/></svg>
      www.deliamarsk.example
    </span>
    <span class="contact__item">
      <svg class="contact__icon" viewBox="0 0 14 14" fill="none" stroke="currentColor"><rect x="1" y="3" width="12" height="8"/><polyline points="1,3 7,8 13,3"/></svg>
      delia@deliamarsk.example
    </span>
  </div>
</section>

<section class="flyer flyer--group">
  <svg class="flyer__art" width="536" height="760" viewBox="0 0 536 760">
    <polygon points="0,276 536,212 536,460 0,610" fill="var(--band-light)"/>
    <rect width="536" height="760" filter="url(#grain)"/>
  </svg>
  <div class="flyer__frame"></div>
  <div class="decor-pieces" role="img" aria-label="Faint dark chess pieces in the background"></div>
  <div class="brand-name">DELIA MARSK</div>
  <div class="figure figure--group" role="img" aria-label="Silhouettes of four people jumping with raised arms"></div>
  <h1 class="program-title">Skyward</h1>
  <svg class="flyer__art" width="536" height="760" viewBox="0 0 536 760">
    <path d="M190 506 Q330 450 476 392" stroke="var(--white)" stroke-width="6" fill="none" stroke-linecap="round"/>
  </svg>
  <p class="program-tagline">Training, Mentoring</p>
  <p class="program-summary">This is one of our highest in-demand programs and is based on a background and proven track record by Delia in accelerating sales organisations and their people into stand out high performers.</p>
  <div class="contact">
    <span class="contact__item">
      <svg class="contact__icon" viewBox="0 0 14 14" fill="none" stroke="currentColor"><circle cx="7" cy="7" r="6"/><ellipse cx="7" cy="7" rx="2.6" ry="6"/><line x1="1" y1="7" x2="13" y2="7"/></svg>
      www.deliamarsk.example
    </span>
    <span class="contact__item">
      <svg class="contact__icon" viewBox="0 0 14 14" fill="none" stroke="currentColor"><rect x="1" y="3" width="12" height="8"/><polyline points="1,3 7,8 13,3"/></svg>
      delia@deliamarsk.example
    </span>
  </div>
</section>
</body>
</html>
```